Venture capital website it shall be called Dalvo Ventures

Venture capital Name is : Dalvo Ventures

i have already regesieted a website and comunicate the details with you when i choose a design.

i need a simple website design for a newly established venture capital. i would like something similar to the websites listed down:

http://www.torvelline.com/

http://www.pilruskaventures.com/

https://qromit.com/

http://www.mudrelcapital.com/

i like mudrel capital the most

Target Market(s)

entrepreneur - startups

Industry/Entity Type

Venture Capital

Number of Pages Required

4 page

Font styles to use
Serif
Sans Serif

Colors
ffc214
fece3e

Requirements
Must have
• the following sections:
• Philosophy (about dalvo Ventures)
• Team
• Knowledge
• address - contact
Nice to have
• http://www.torvelline.com/
• http://www.pilruskaventures.com/
• https://qromit.com/
• http://www.mudrelcapital.com/

```html
<!DOCTYPE html>
<html lang="en">
<head>
<meta charset="utf-8">
<title>Dalvo Ventures — Knowledge</title>
<link rel="stylesheet" href="https://fonts.googleapis.com/css2?family=Cinzel:wght@700&family=Roboto:wght@300;400&display=swap">
<style>
  :root {
    --brand-yellow: #ffc214;
    --white: #ffffff;
    --ink: #111111;
    --muted: #555555;
    --accent-blue: #0aa0f0;
    --chart-deep: #34607f;
    --chart-soft: #e9eef3;
    --nav-button: #b5a03a;
  }
  * { margin: 0; padding: 0; box-sizing: border-box; }
  html, body { width: 1148px; height: 1200px; overflow: hidden; background: var(--white); }
  body { position: relative; font-family: "Roboto", Arial, sans-serif; color: var(--ink); }

  .site-header { position: absolute; left: 0; top: 0; width: 1148px; height: 166px; background: var(--brand-yellow); }
  .main-nav a {
    position: absolute; top: 75px; font-family: "Cinzel", Georgia, serif; font-weight: 700;
    font-size: 29.5px; color: var(--white); text-decoration: none; padding-bottom: 3px;
    border-bottom: 3px solid var(--ink); letter-spacing: 0.5px;
  }
  .main-nav a.is-current { color: var(--ink); }
  .nav-philosophy { left: 103px; }
  .nav-team { left: 390px; }
  .nav-knowledge { left: 589px; }
  .nav-contact { left: 877px; }

  .activity-chart {
    position: absolute; left: 91px; top: 234px; width: 401px; height: 351px;
    background: linear-gradient(180deg, var(--chart-soft) 0%, #c9d6e2 55%, var(--chart-deep) 100%);
  }
  .chart-source { position: absolute; left: 225px; top: 599px; font-size: 18.5px; font-weight: 300; }

  .advantages { position: absolute; left: 603px; top: 228px; width: 520px; }
  .advantages h2 { font-size: 17px; font-weight: 400; letter-spacing: 0.4px; margin-bottom: 22px; }
  .advantages ul { list-style: none; font-size: 15px; font-weight: 300; line-height: 18px; }
  .advantages li::before { content: "\2663"; margin-right: 6px; }

  .target-heading { position: absolute; left: 601px; top: 466px; display: flex; align-items: center; }
  .target-heading .marker { width: 78px; height: 28px; background: var(--accent-blue); }
  .target-heading h2 { font-size: 23.5px; font-weight: 400; margin-left: 18px; }

  .market-size { position: absolute; left: 598px; top: 533px; width: 500px; font-size: 15.5px; line-height: 20.4px; color: var(--muted); letter-spacing: -0.2px; }

  .startup-criteria, .involvement { position: absolute; font-size: 19.8px; font-weight: 300; line-height: 23.7px; list-style: none; }
  .startup-criteria { left: 96px; top: 844px; }
  .involvement { left: 603px; top: 844px; width: 445px; }

  .scroll-control { position: absolute; left: 21px; top: 1089px; }
</style>
</head>
<body>
<header class="site-header">
  <nav class="main-nav">
    <a class="nav-philosophy" href="#">PHILOSOPHY</a>
    <a class="nav-team" href="#">TEAM</a>
    <a class="nav-knowledge is-current" href="#">KNOWLEDGE</a>
    <a class="nav-contact" href="#">CONTACT</a>
  </nav>
</header>

<div class="activity-chart" role="img" aria-label="Chart of yearly venture capital deal value and number of deals closed"></div>
<p class="chart-source">Source: VCTA</p>

<section class="advantages">
  <h2>DALVO VENTURES COMPETITIVE ADVANTAGES</h2>
  <ul>
    <li>Congenial customer service</li>
    <li>Vast Industry Network</li>
    <li>Experienced, competent and professional management</li>
    <li>In-house expertise in key-technical areas</li>
    <li>Connection and influence</li>
    <li>Investment banking background of founders</li>
    <li>Capable investors</li>
  </ul>
</section>

<div class="target-heading"><span class="marker"></span><h2>Target Market</h2></div>

<p class="market-size">Market Size: The Company is entering the market at a time when the industry is experiencing substantial growth. According to market research firm Tarnley Research, the Venture Capital Industry has seen an average annual growth rate of 6.3% over the last five years, positioning industry revenue to be around $30.2 billion in 2014. These trends are expected to continue over the next several years, as is the overall growth in the industry. The Venture Capital industry is projected to see an average annual growth rate of 3.9% over the next three years, placing industry revenue at $36.6 billion in 2019. These trends bode extremely well for organizations such as Dalvo Venture Capital, as they show the long-term potential investment opportunities.</p>

<ul class="startup-criteria">
  <li>Criteria for Potential Start-ups:</li>
  <li>• Early Stage Start-ups (not Seed Stage)</li>
  <li>• Strong Management</li>
  <li>• Promising Product</li>
  <li>• Unified Partners and Board of Directors</li>
</ul>

<ul class="involvement">
  <li>• Participate in the Board of Directors (BOD)</li>
  <li>• Create a Synergy with Existing Investments and Partners</li>
  <li>• Provide the management with</li>
  <li>o Expansion Plan</li>
  <li>o Assistance and Implementation Guidelines</li>
  <li>• Provide Technical Support</li>
  <li>• Provide Managerial Support</li>
  <li>• Provide Connections and Influence</li>
  <li>• Provide Financial Support</li>
  <li>• Exit from the Stake</li>
  <li>o Selling Stake</li>
  <li>o Initial Public Offering (IPO)</li>
</ul>

<svg class="scroll-control" width="82" height="82" viewBox="0 0 82 82" aria-label="Page navigation">
  <circle cx="41" cy="41" r="41" fill="var(--nav-button)"/>
  <polygon points="41,13 50,24 32,24" fill="#fff"/>
  <polygon points="41,69 50,58 32,58" fill="#fff"/>
  <polygon points="12,41 23,32 23,50" fill="#fff"/>
</svg>
</body>
</html>
```